Brochure Design For Beauty Salon

We have an existing brochure for our beauty salon business which has been designed in-house.

We need a designer to refresh the look and feel of the brochure, which is intended for print. The print format will be 210mmx210mm (square, stapled).

We need a design for each and every page of the brochure, including the front and back covers.

We are looking for a fresh modern design, quite close to what we already have, but looking more slick and professional.

The primary colors are white, grey and purple. The final design will communicate luxury, prestige and cleanliness and have a heavy focus on creating the feeling of space within each page.

Target Market(s)

Professional Women, aged 20-45

Industry/Entity Type

Beauty Salon

Font styles to use
Sans Serif
Other font styles liked:
• Helvetica

Requirements
Must have
• The project must be ready for print on square paper 210x210mm

```html
<!DOCTYPE html>
<html lang="en">
<head>
<meta charset="utf-8">
<title>Lumi Rae Treatment Menu</title>
<link href="https://fonts.googleapis.com/css2?family=Montserrat:wght@400;600;700;800;900&family=Questrial&display=swap" rel="stylesheet">
<style>
  :root{
    --plum:#6e1a3e;
    --plum-dark:#5a1230;
    --plum-band:#7a2447;
    --white:#ffffff;
    --paper:#f7f7f7;
    --grey:#7d7d7d;
    --grey-light:#dcdcdc;
    --text:#555555;
    --stage:#eceeef;
  }
  *{box-sizing:border-box;margin:0;padding:0}
  html,body{width:901px;height:1200px;overflow:hidden;background:var(--stage)}
  body{position:relative;font-family:"Montserrat",sans-serif}

  /* Front cover */
  .cover{position:absolute;left:170px;top:34px;width:528px;height:526px;background:var(--plum-dark)}
  .cover-photo{position:absolute;left:19px;top:19px;width:490px;height:433px;
    background:radial-gradient(ellipse at 45% 35%,#e8c6b8 0%,#c98c9a 30%,#6b3f6a 60%,#2a1a2e 100%)}
  .cover-url{position:absolute;left:346px;top:301px;width:148px;height:26px;border:1px solid var(--white);
    color:var(--white);font-weight:700;font-size:11.5px;letter-spacing:.5px;display:flex;align-items:center;justify-content:center}
  .cover-band{position:absolute;left:0;top:418px;width:528px;height:70px;display:flex}
  .cover-name{width:112px;background:var(--grey-light);display:flex;align-items:center;justify-content:center;
    font-family:"Questrial",sans-serif;font-size:22px;line-height:1;color:var(--plum);text-align:center}
  .cover-title{flex:1;background:var(--plum-band);color:var(--white);font-weight:900;font-size:29px;
    letter-spacing:2.5px;display:flex;align-items:center;justify-content:center;padding-left:6px}
  .cover-band-end{width:20px;background:var(--grey-light)}

  /* Open spread */
  .spread{position:absolute;left:54px;top:682px;width:808px;height:414px;background:var(--paper);
    box-shadow:0 2px 6px rgba(0,0,0,.12)}
  .spread-photo{position:absolute;left:0;top:0;width:602px;height:414px;
    background:radial-gradient(ellipse at 40% 38%,#e9c8ae 0%,#c78a60 22%,#a9b64a 50%,#6f9a2e 78%,#4d7a22 100%)}
  .gutter{position:absolute;left:403px;top:0;width:2px;height:414px;background:linear-gradient(90deg,rgba(0,0,0,.12),rgba(0,0,0,0))}

  .tagline{position:absolute;left:12px;top:343px;width:318px;height:51px;background:var(--plum-band);color:var(--white)}
  .tagline-top{position:absolute;left:31px;top:9px;font-size:10px;font-weight:600;letter-spacing:3.2px}
  .tagline-bottom{position:absolute;right:8px;top:28px;font-size:13.5px;font-weight:700;letter-spacing:2.5px}
  .tagline-rule{position:absolute;height:1px;background:rgba(255,255,255,.7)}

  .text-panel{position:absolute;left:482px;top:110px;width:326px;height:304px;background:var(--white)}
  .text-panel-top{position:absolute;left:598px;top:0;width:210px;height:110px;background:var(--white)}
  .section-title{position:absolute;left:18px;top:38px;color:var(--plum);font-weight:900;font-size:21px;
    line-height:29px;letter-spacing:2px}
  .title-rule{position:absolute;left:18px;top:110px;width:68px;height:3px;background:var(--grey)}
  .intro{position:absolute;left:18px;top:136px;width:270px;font-size:7.4px;line-height:11.6px;color:var(--text)}
  .treatment{position:absolute;left:18px;top:190px;width:270px}
  .treatment-head{display:flex;justify-content:space-between;font-size:7.6px;font-weight:700;color:#444;
    padding-bottom:4px;border-bottom:1px solid var(--grey-light);position:relative}
  .treatment-head::after{content:"";position:absolute;right:0;bottom:-2px;width:70px;height:2px;background:var(--plum)}
  .treatment-price{letter-spacing:.5px}
  .treatment-desc{margin-top:10px;font-size:7.4px;line-height:11.6px;color:var(--text)}
</style>
</head>
<body>

<section class="cover">
  <div class="cover-photo" role="img" aria-label="Glamour portrait of a woman with dark wavy hair and magenta lipstick"></div>
  <div class="cover-url">www.lumirae.co.uk</div>
  <div class="cover-band">
    <div class="cover-name">Lumi<br>Rae</div>
    <div class="cover-title">TREATMENT MENU</div>
    <div class="cover-band-end"></div>
  </div>
</section>

<section class="spread">
  <div class="spread-photo" role="img" aria-label="Smiling woman with auburn hair among sunlit green leaves"></div>
  <div class="gutter"></div>

  <div class="tagline">
    <span class="tagline-top">UNDERSTAND YOUR SKIN</span>
    <span class="tagline-rule" style="left:232px;top:15px;width:80px"></span>
    <span class="tagline-rule" style="left:0;top:38px;width:190px"></span>
    <span class="tagline-bottom">LIKE WE DO</span>
  </div>

  <div class="text-panel-top"></div>
  <div class="text-panel">
    <h2 class="section-title">VELOURA<br>FACIALS</h2>
    <div class="title-rule"></div>
    <p class="intro">The results you are going to see with a Veloura® skin treatment are unlike anything else in the industry because we exfoliate the skin, we double cleanse the skin, we do extractions, tailor-made customized massage and masque technique.</p>
    <div class="treatment">
      <div class="treatment-head"><span>Skin Reset®</span><span class="treatment-price">£10 | 10 mins</span></div>
      <p class="treatment-desc">Test-drive your prescribed regimen under the guidance of a professional Skin Therapist. At Skin Studio®, you can learn about your skin with Skin Charting®, and then learn how to use the products, hands-on.</p>
    </div>
  </div>
</section>

</body>
</html>
```